Online Digital Solutions Agency needs a New Business Card

We are a Online/Digital solution agency. We provide WordPress Solutions, Online & Digital Marketing Solutions including SEO, Social Media Marketing and Managed Hosting including VPS and Cloud Hosting solutions. We also design and build bespoke web sites and web applications for various clients. We are very good at site migrations, 3rd party API integrations and mobile app development.

We are rebranding our agency and have already designed a new logo. We have selected 5-6 colours as our base colour and are currently building our new website based around these colour scheme.

Our logo indicates that we are a cloud solution providers, and (i.e. the Clouds), and developers (i.e. HTML Tags, and CSS formats). We use the 5-6 base colours and use various shades of these colours as required.

Our old website is located at: www.brambleforgelabs.com

And our new website is going to be at (we are working on it at the moment ...):
https://creative.brambleforgelabs.co.uk/

Our slogan is "Digital Transformation Specialist"

What we mean by that is; we can take any existing business and get them up and transform them in to the digital world, starting with Hosting, Web Design, Development & Online Marketing aspects.

The powerpoint is a document that we use to present our projects to clients at the moment, and the cloud is on the background as we clarified earlier. (Just to get the idea)

What we are looking for is a Great WoW factor design to start with, ideally with the Logo and Logo colour scheme if possible but not required as long as the designers can do better, and basically give life to our logo and company via the Business card design.

Ideally with some icons perhaps to indicate the address, location, mobile, email, and website would be good but again optional as long as there is a good design.

The cloud can be used as a background if required in a light shade or as a watermark share perhaps.

The logos' and the Illustrator files are shared with you so you can use them as required.

Ideally the business card should have a Name, title, Mobile, Email , Website, Address and perhaps some social media links.

Target Market(s)

New Startups, SME's, Contract and Outsource Clients

Contact Information for Business Card

Company Name:
==============
BrambleForge Labs (UK) Ltd.

Tag Line:
========
“Digital Transformation Specialists”

Adress:
=======

Suite KR73054
14-16 Ashgrove Lane
London
E9 4PD.

Name:
=====
Idris Malek

Title: (Optional)
=============
FQTA, PgD (RNOM)

Role:
=====
Digital Solutions Architect

Email:
=====
idris@brambleforgelabs.uk

WebSite:
=======
http://www.brambleforgelabs.uk

OR

www.brambleforgelabs.uk

Mobile:
======
0044 (0)75 218 30479

OR

+44 (0)75 218 30479

LinkedIN: (Optional)
========
https://uk.linkedin.com/in/idrismalek

Skype: (Optional)
======
idris.malek

Twitter (Optional) : idrismalek

Font styles to use
Serif
Sans Serif

Requirements
Must have
• The Logo
• Business Name
• Person Name
• Title
• Mobile
• Email
• Website
• Address
• I have provided the colour scheme on my files.
Nice to have
• Twiter
• Linked in
• Facebook

```html
<!DOCTYPE html>
<html lang="en">
<head>
<meta charset="utf-8">
<title>BrambleForge Labs – Business Card</title>
<link href="https://fonts.googleapis.com/css2?family=Source+Sans+3:wght@400;600;700&display=swap" rel="stylesheet">
<style>
  :root {
    --bg: #2b2b2d;
    --card: #121213;
    --card-edge: #1c1c1e;
    --band: #1463c4;
    --brand: #1f73c9;
    --cyan: #2fb0e6;
    --text: #e8e8e8;
    --muted: #cfcfcf;
    --divider: #3a3a3c;
  }
  * { box-sizing: border-box; margin: 0; padding: 0; }
  html, body { width: 1200px; height: 900px; overflow: hidden; }
  body {
    background: var(--bg);
    font-family: "Source Sans 3", "Myriad Pro", Arial, sans-serif;
    color: var(--text);
    position: relative;
  }
  .card {
    position: absolute;
    left: 340px;
    width: 520px;
    height: 300px;
    background: linear-gradient(160deg, var(--card-edge), var(--card) 60%);
    border-bottom: 9px solid var(--band);
    box-shadow: 0 18px 40px rgba(0,0,0,.45);
  }
  .card--front { top: 100px; }
  .card--back { top: 480px; }

  /* front */
  .brand {
    position: absolute;
    top: 92px; left: 0; right: 0;
    display: flex; justify-content: center; align-items: center; gap: 12px;
  }
  .brand__mark { width: 22px; height: 22px; border-radius: 50%; background: var(--cyan); }
  .brand__name {
    font-weight: 700; font-size: 44px; color: var(--brand); letter-spacing: .5px; line-height: 1.2;
  }
  .tagline {
    position: absolute; top: 160px; left: 0; right: 0;
    text-align: center; font-weight: 600; font-size: 15px; letter-spacing: 1.5px;
    text-transform: uppercase; color: var(--muted);
  }
  .socials {
    position: absolute; bottom: 22px; left: 30px; right: 30px;
    display: flex; justify-content: space-between; align-items: center;
    font-size: 15px; color: var(--text); white-space: nowrap;
  }
  .socials__group { display: flex; gap: 22px; }
  .social { display: flex; align-items: center; gap: 7px; }
  .social__dot { width: 15px; height: 15px; background: var(--band); border-radius: 2px; flex: none; }

  /* back */
  .person {
    position: absolute; top: 86px; right: 290px; text-align: right; white-space: nowrap;
  }
  .person__name {
    font-weight: 700; font-size: 25px; color: var(--cyan); letter-spacing: 1.5px; line-height: 1;
  }
  .person__role { font-size: 15px; color: var(--muted); margin-top: 3px; }
  .divider {
    position: absolute; left: 250px; top: 84px; width: 1px; height: 90px; background: var(--divider);
  }
  .contacts {
    position: absolute; left: 268px; top: 92px; list-style: none;
    font-size: 15px; line-height: 20px; white-space: nowrap;
  }
  .contacts li { display: flex; align-items: center; gap: 8px; }
  .contacts svg { width: 13px; height: 13px; fill: var(--cyan); flex: none; }
  .address {
    position: absolute; left: 60px; bottom: 32px; font-size: 17px; color: var(--text); white-space: nowrap;
  }
</style>
</head>
<body>
  <section class="card card--front">
    <div class="brand">
      <span class="brand__mark"></span>
      <span class="brand__name">BrambleForge Labs</span>
    </div>
    <p class="tagline">Digital Transformation Specialists</p>
    <div class="socials">
      <span class="social"><span class="social__dot"></span>www.profilehub.net/in/idrismalek</span>
      <span class="socials__group">
        <span class="social"><span class="social__dot"></span>idris.malek</span>
        <span class="social"><span class="social__dot"></span>idrismalek</span>
      </span>
    </div>
  </section>

  <section class="card card--back">
    <div class="person">
      <h1 class="person__name">IDRIS MALEK</h1>
      <p class="person__role">Digital Solutions Architect</p>
    </div>
    <div class="divider"></div>
    <ul class="contacts">
      <li><svg viewBox="0 0 16 16"><path d="M3 1h3l1.5 4-2 1.3a9 9 0 0 0 4.2 4.2L11 8.5l4 1.5v3a2 2 0 0 1-2 2C6.4 15 1 9.6 1 3a2 2 0 0 1 2-2z"/></svg>+44 (0)75 218 30479</li>
      <li><svg viewBox="0 0 16 16"><path d="M4.5 0h7A1.5 1.5 0 0 1 13 1.5v13a1.5 1.5 0 0 1-1.5 1.5h-7A1.5 1.5 0 0 1 3 14.5v-13A1.5 1.5 0 0 1 4.5 0zM5 2v10h6V2zm3 11a1 1 0 1 0 0 2 1 1 0 0 0 0-2z"/></svg>0044 (0)75 218 30479</li>
      <li><svg viewBox="0 0 16 16"><path d="M0 3h16v10H0zm1.5 1.2V5l6.5 4 6.5-4v-.8L8 8z"/></svg>idris@brambleforgelabs.uk</li>
      <li><svg viewBox="0 0 16 16"><circle cx="8" cy="8" r="7.5"/><path d="M1 8h14M8 .5c-3 3.5-3 11.5 0 15M8 .5c3 3.5 3 11.5 0 15" stroke="#121213" stroke-width="1.2" fill="none"/></svg>www.brambleforgelabs.uk</li>
    </ul>
    <p class="address">14-16, Ashgrove Lane London, E9 4PD United Kingdom</p>
  </section>
</body>
</html>
```